Business Card Design Project

Double-side business card.
Side One:
Logo (Including the word TOLVEKA that is part of the Logo
"Programas de Renovación Urbana y Cuidado del Entorno Natural Andino"
Side Two:
Marcela Ostrander
Co-Founder & CEO
Washington, DC (USA)
email: marcelao@tolveka.example (please use an icon for "emal")
cell: +1 (202) 555 0147 (please use an icon for "cell")
skype: marceostrander (please use an icon for "skype")
twitter: marceostrander (please use an icon for "twitter")
www.tolveka.example
Target Market(s)
Foundations, Governments, and Private sector companies that implement projects for sustainability.
Industry/Entity Type
Business
Font styles to use
Colors
Designer to choose colors to be used in the design.
Requirements
Nice to have
- barcode

```html
<!DOCTYPE html>
<html lang="es">
<head>
<meta charset="utf-8">
<title>TOLVEKA — Business Card</title>
<link href="https://fonts.googleapis.com/css2?family=Exo+2:wght@400;500&display=swap" rel="stylesheet">
<style>
  :root {
    --backdrop: #2b2b2d;
    --card: #f6f6f6;
    --ink-grey: #858789;
    --ink-red: #ee5a45;
    --warm-light: #f2a07a;
    --warm-mid: #e6683f;
    --warm-deep: #d0603a;
  }
  * { margin: 0; padding: 0; box-sizing: border-box; }
  html, body { width: 1200px; height: 798px; overflow: hidden; }
  body {
    background: var(--backdrop);
    font-family: "Exo 2", sans-serif;
    display: flex;
    align-items: center;
    justify-content: center;
    gap: 40px;
  }
  .card {
    position: relative;
    width: 540px;
    height: 309px;
    background: var(--card);
    border-radius: 4px;
    overflow: hidden;
  }
  .card svg.accent { position: absolute; inset: 0; }

  /* Front */
  .brand {
    position: absolute;
    left: 0; right: 0; top: 78px;
    text-align: center;
  }
  .brand-name {
    display: inline-flex;
    align-items: center;
    gap: 14px;
    font-size: 62px;
    font-weight: 400;
    letter-spacing: 4px;
    color: var(--ink-grey);
    line-height: 1;
  }
  .brand-mark {
    width: 22px; height: 22px;
    background: var(--warm-mid);
    display: inline-block;
  }
  .tagline {
    margin-top: 12px;
    font-size: 17px;
    line-height: 1.2;
    color: var(--ink-red);
  }

  /* Back */
  .person {
    position: absolute;
    left: 78px; top: 34px;
  }
  .person-name {
    font-size: 36px;
    font-weight: 500;
    color: var(--ink-grey);
    line-height: 1.05;
  }
  .person-role {
    font-size: 22px;
    color: var(--ink-red);
    margin-bottom: 18px;
  }
  .contact-list { list-style: none; }
  .contact-list li {
    display: flex;
    align-items: center;
    gap: 12px;
    font-size: 19px;
    color: var(--ink-grey);
    line-height: 1.45;
  }
  .contact-icon {
    width: 18px; height: 18px;
    flex: none;
  }
</style>
</head>
<body>

  <section class="card card-front" aria-label="Business card front">
    <svg class="accent" viewBox="0 0 540 309" role="img" aria-label="Warm colour accent band along the bottom edge">
      <defs>
        <linearGradient id="front-accent" x1="0" y1="0" x2="1" y2="0">
          <stop offset="0" stop-color="var(--warm-light)"/>
          <stop offset="0.5" stop-color="var(--warm-mid)"/>
          <stop offset="1" stop-color="var(--warm-deep)"/>
        </linearGradient>
      </defs>
      <path d="M0 262 L540 292 L540 309 L0 309 Z" fill="url(#front-accent)"/>
    </svg>
    <div class="brand">
      <div class="brand-name"><span class="brand-mark"></span>TOLVEKA</div>
      <p class="tagline">Programas de Renovación Urbana y<br>Cuidado del Entorno Natural Andino</p>
    </div>
  </section>

  <section class="card card-back" aria-label="Business card back">
    <svg class="accent" viewBox="0 0 540 309" role="img" aria-label="Warm colour accent strip along the left edge">
      <defs>
        <linearGradient id="back-accent" x1="0" y1="0" x2="0" y2="1">
          <stop offset="0" stop-color="var(--warm-deep)"/>
          <stop offset="1" stop-color="var(--warm-light)"/>
        </linearGradient>
      </defs>
      <rect x="0" y="0" width="12" height="309" fill="url(#back-accent)"/>
    </svg>
    <div class="person">
      <h1 class="person-name">Marcela Ostrander</h1>
      <p class="person-role">Co-Founder &amp; CEO</p>
      <ul class="contact-list">
        <li>
          <svg class="contact-icon" viewBox="0 0 18 18" aria-label="email">
            <circle cx="9" cy="9" r="8" fill="none" stroke="var(--ink-red)" stroke-width="1.5"/>
            <rect x="5" y="6" width="8" height="6" fill="none" stroke="var(--ink-red)" stroke-width="1.2"/>
            <path d="M5 6 L9 9.5 L13 6" fill="none" stroke="var(--ink-red)" stroke-width="1.2"/>
          </svg>
          marcelao@tolveka.example
        </li>
        <li>
          <svg class="contact-icon" viewBox="0 0 18 18" aria-label="cell">
            <circle cx="9" cy="9" r="8" fill="none" stroke="var(--ink-red)" stroke-width="1.5"/>
            <rect x="6.5" y="4.5" width="5" height="9" rx="1" fill="none" stroke="var(--ink-red)" stroke-width="1.2"/>
            <circle cx="9" cy="11.6" r="0.7" fill="var(--ink-red)"/>
          </svg>
          +1 (202) 555 0147
        </li>
        <li>
          <svg class="contact-icon" viewBox="0 0 18 18" aria-label="skype">
            <circle cx="9" cy="9" r="8" fill="none" stroke="var(--ink-red)" stroke-width="1.5"/>
          </svg>
          marceostrander
        </li>
        <li>
          <svg class="contact-icon" viewBox="0 0 18 18" aria-label="twitter">
            <circle cx="9" cy="9" r="8" fill="none" stroke="var(--ink-red)" stroke-width="1.5"/>
          </svg>
          marceostrander
        </li>
        <li>
          <svg class="contact-icon" viewBox="0 0 18 18" aria-label="web">
            <circle cx="9" cy="9" r="8" fill="none" stroke="var(--ink-red)" stroke-width="1.5"/>
            <circle cx="9" cy="9" r="4" fill="none" stroke="var(--ink-red)" stroke-width="1.1"/>
            <path d="M5 9 H13 M9 5 V13" stroke="var(--ink-red)" stroke-width="1.1"/>
          </svg>
          www.tolveka.example
        </li>
      </ul>
    </div>
  </section>

</body>
</html>
```